Timeline flyer

Hi, we are an agency, our business is to orienteates student to study abroad in Germany. For that, we enroll them in language schools in Germany and help them to find an accomodation.
Students are always lost we thinked about a timeline to help them figure out what they have to do once in Germany so they don't miss delays.
You can find in the attachement an example that i made in powerpoint but it's really basic and it's only for u so you can understant what the timeline should look like.
We need two time lines.
For the first one (file first timeline)
Title : Procédure pour intégrer le semestre d’hiver dans les universités Allemandes
The first paragraph (up on the left in my proposition) : L’étudiant devra pendant ces mois débuter ses cours d’allemand en Tunisie et les poursuivre en Allemagne après l’obtention du Visa d’étude. L’atteinte du niveau C1 est primordiale pour la bonne réussite du test Kel ou le MRT.
The second paragraph (below on the left in my proposition) : L’étudiant devra à cette date avoir déjà passer le test KEL ou le MRT pour pouvoir être à temps pour les inscriptions universitaires. Il faut compter 6 semaines pour le test Kel et 2 à 3 semaines pour obtenir les résultats des tests.
The third one (up on the right in my proposition) : Le dernier délais d’inscription pour pouvoir intégrer une université Allemande pendant la rentrée hivernale (15 Octobre).
The last one (below on the right in my proposition) : Rentrée universitaire
For the second one (file second timeline) :
Title : Procédure pour intégrer le semestre d’été dans les universités Allemandes *
The third one (up on the right in my proposition) : Le dernier délais d’inscription pour pouvoir intégrer une université Allemande pendant la rentrée estivale (15 Avril).
There is also an additional sentence below in the right for this one : * Les spécialités assurées pendant les semestres d’été sont limitées.
You can also find in the attachement our flyers (so you can inspire youself with the color and the design), we want our student to recognize that the flyer is related to our agency so please try to use colors that are matched with the other flyer.
Also, you can find our Logo in the attachement.
Thank you :)
Waiting for your propositions ! :)

```html
<!DOCTYPE html>
<html lang="fr">
<head>
<meta charset="utf-8">
<title>Procédure pour intégrer le semestre d’hiver dans les universités Allemandes</title>
<link rel="stylesheet" href="https://fonts.googleapis.com/css2?family=Arimo:wght@400;700&display=swap">
<style>
  :root {
    --page: #ebe6de;
    --card: #ffffff;
    --panel: #c5dfe0;
    --lime: #c8d42b;
    --teal: #3a9398;
    --ink: #37474f;
    --text: #111111;
  }
  html, body {
    margin: 0;
    width: 1200px;
    height: 1200px;
    overflow: hidden;
    background: var(--page);
  }
  .flyer { display: block; width: 1200px; height: 1200px; font-family: "Arimo", Arial, sans-serif; }
  .card { fill: var(--card); }
  .panel { fill: var(--panel); }
  .title { font-weight: 700; font-size: 50px; fill: var(--text); }
  .brand-name { font-weight: 700; font-size: 40px; fill: var(--lime); }
  .brand-dot { fill: var(--lime); }
  .axis { stroke: var(--ink); stroke-width: 5; }
  .connector { stroke: var(--ink); stroke-width: 2; fill: none; }
  .tick { stroke: var(--ink); stroke-width: 2; }
  .node { fill: var(--teal); stroke: var(--ink); stroke-width: 4; }
  .month { font-size: 18px; fill: var(--text); text-anchor: middle; }
  .milestone { fill: var(--teal); stroke: var(--ink); stroke-width: 5; }
  .milestone-text { font-size: 23px; fill: #ffffff; text-anchor: middle; }
  .note { fill: var(--lime); stroke: var(--ink); stroke-width: 2; }
  .note-text { font-size: 21.5px; fill: var(--text); }
  .icon-tile { fill: var(--ink); }
  .icon-line { stroke: #ffffff; stroke-width: 2.5; fill: none; stroke-linecap: round; stroke-linejoin: round; }
</style>
</head>
<body>
<svg class="flyer" viewBox="0 0 1500 1500" xmlns="http://www.w3.org/2000/svg">
  <!-- card -->
  <rect class="card" x="50" y="262" width="1400" height="976"/>

  <g class="header">
    <text class="title" x="135" y="352">Procédure pour intégrer le semestre d’hiver</text>
    <text class="title" x="135" y="418">dans les universités Allemandes</text>
    <g class="brand">
      <circle class="brand-dot" cx="1290" cy="366" r="14"/>
      <text class="brand-name" x="1314" y="370">Neuweg</text>
      <text class="brand-name" x="1314" y="410" style="font-size:24px">centre</text>
    </g>
  </g>

  <rect class="panel" x="50" y="460" width="1400" height="695"/>

  <!-- connectors -->
  <line class="connector" x1="147" y1="682" x2="147" y2="765"/>
  <line class="connector" x1="750" y1="682" x2="750" y2="765"/>
  <line class="connector" x1="1008" y1="620" x2="1008" y2="765"/>
  <polyline class="connector" points="697,982 835,982 835,768"/>
  <line class="connector" x1="1266" y1="768" x2="1266" y2="926"/>

  <line class="axis" x1="50" y1="765" x2="1450" y2="765"/>

  <!-- milestones -->
  <g class="milestone-box">
    <rect class="milestone" x="783" y="632" width="105" height="130"/>
    <text class="milestone-text" x="835" y="676">Début</text>
    <text class="milestone-text" x="835" y="704">Mai</text>
    <text class="milestone-text" x="835" y="732">2017</text>
  </g>
  <g class="milestone-box">
    <rect class="milestone" x="955" y="767" width="104" height="128"/>
    <text class="milestone-text" x="1007" y="815">15</text>
    <text class="milestone-text" x="1007" y="843">Juillet</text>
    <text class="milestone-text" x="1007" y="871">2017</text>
  </g>
  <g class="milestone-box">
    <rect class="milestone" x="1214" y="632" width="104" height="130"/>
    <text class="milestone-text" x="1266" y="679">15</text>
    <text class="milestone-text" x="1266" y="707">Octobre</text>
    <text class="milestone-text" x="1266" y="735">2017</text>
  </g>

  <!-- month nodes -->
  <g class="months">
    <g><line class="tick" x1="147" y1="778" x2="147" y2="795"/><line class="tick" x1="137" y1="795" x2="157" y2="795"/><circle class="node" cx="147" cy="765" r="13"/><text class="month" x="147" y="826">Sep</text><text class="month" x="147" y="848">2016</text></g>
    <g><line class="tick" x1="233" y1="778" x2="233" y2="795"/><line class="tick" x1="223" y1="795" x2="243" y2="795"/><circle class="node" cx="233" cy="765" r="13"/><text class="month" x="233" y="826">Oct</text><text class="month" x="233" y="848">2016</text></g>
    <g><line class="tick" x1="319" y1="778" x2="319" y2="795"/><line class="tick" x1="309" y1="795" x2="329" y2="795"/><circle class="node" cx="319" cy="765" r="13"/><text class="month" x="319" y="826">Nov</text><text class="month" x="319" y="848">2016</text></g>
    <g><line class="tick" x1="405" y1="778" x2="405" y2="795"/><line class="tick" x1="395" y1="795" x2="415" y2="795"/><circle class="node" cx="405" cy="765" r="13"/><text class="month" x="405" y="826">Déc</text><text class="month" x="405" y="848">2016</text></g>
    <g><line class="tick" x1="491" y1="778" x2="491" y2="795"/><line class="tick" x1="481" y1="795" x2="501" y2="795"/><circle class="node" cx="491" cy="765" r="13"/><text class="month" x="491" y="826">Jan</text><text class="month" x="491" y="848">2016</text></g>
    <g><line class="tick" x1="578" y1="778" x2="578" y2="795"/><line class="tick" x1="568" y1="795" x2="588" y2="795"/><circle class="node" cx="578" cy="765" r="13"/><text class="month" x="578" y="826">Fév</text><text class="month" x="578" y="848">2016</text></g>
    <g><line class="tick" x1="664" y1="778" x2="664" y2="795"/><line class="tick" x1="654" y1="795" x2="674" y2="795"/><circle class="node" cx="664" cy="765" r="13"/><text class="month" x="664" y="826">Mars</text><text class="month" x="664" y="848">2016</text></g>
    <g><line class="tick" x1="750" y1="778" x2="750" y2="795"/><line class="tick" x1="740" y1="795" x2="760" y2="795"/><circle class="node" cx="750" cy="765" r="13"/><text class="month" x="750" y="826">Avr</text><text class="month" x="750" y="848">2016</text></g>
    <circle class="node" cx="835" cy="767" r="13"/>
    <g><line class="tick" x1="921" y1="778" x2="921" y2="795"/><line class="tick" x1="911" y1="795" x2="931" y2="795"/><circle class="node" cx="921" cy="765" r="13"/><text class="month" x="917" y="826">Jui</text><text class="month" x="917" y="848">2017</text></g>
    <circle class="node" cx="1008" cy="765" r="13"/>
    <g><line class="tick" x1="1094" y1="778" x2="1094" y2="795"/><line class="tick" x1="1084" y1="795" x2="1104" y2="795"/><circle class="node" cx="1094" cy="765" r="13"/><text class="month" x="1093" y="826">Août</text><text class="month" x="1093" y="848">2017</text></g>
    <g><line class="tick" x1="1180" y1="778" x2="1180" y2="795"/><line class="tick" x1="1170" y1="795" x2="1190" y2="795"/><circle class="node" cx="1180" cy="765" r="13"/><text class="month" x="1179" y="826">Sep</text><text class="month" x="1179" y="848">2017</text></g>
    <circle class="node" cx="1266" cy="767" r="13"/>
    <g><line class="tick" x1="1352" y1="778" x2="1352" y2="795"/><line class="tick" x1="1342" y1="795" x2="1362" y2="795"/><circle class="node" cx="1352" cy="765" r="13"/><text class="month" x="1351" y="826">Nov</text><text class="month" x="1351" y="848">2017</text></g>
  </g>

  <!-- note: language courses -->
  <g class="note-box">
    <path class="note" d="M147,492 H750 V682 H662 L645,664 L628,682 H147 Z"/>
    <text class="note-text">
      <tspan x="168" y="524">L’étudiant devra pendant ces mois débuter</tspan>
      <tspan x="168" y="552">ses cours d’allemand en Tunisie et les</tspan>
      <tspan x="168" y="580">poursuivre en Allemagne après l’obtention</tspan>
      <tspan x="168" y="608">du Visa d’étude. L’atteinte du niveau C1 est</tspan>
      <tspan x="168" y="636">primordiale pour la bonne réussite du test</tspan>
      <tspan x="168" y="664">Kel ou le MRT.</tspan>
    </text>
    <rect class="icon-tile" x="645" y="505" width="85" height="83" rx="5"/>
    <g class="icon-line">
      <circle cx="667" cy="521" r="4"/>
      <path d="M667,527 V552 H680 V570"/>
      <path d="M676,540 H714 M692,540 V572 M684,572 H700 M710,540 V572"/>
    </g>
  </g>

  <!-- note: registration deadline -->
  <g class="note-box">
    <path class="note" d="M773,492 H1352 V600 H1026 L1008,620 L990,600 H773 Z"/>
    <text class="note-text">
      <tspan x="794" y="526">Le dernier délais d’inscription pour</tspan>
      <tspan x="794" y="554">pouvoir intégrer une université Allemande</tspan>
      <tspan x="794" y="582">pendant la rentrée hivernale (15 Octobre).</tspan>
    </text>
    <rect class="icon-tile" x="1248" y="505" width="84" height="83" rx="5"/>
    <g class="icon-line">
      <path d="M1306,550 V572 H1264 V518 H1300 L1306,524"/>
      <path d="M1272,532 H1294 M1272,541 H1294 M1272,550 H1290 M1272,559 H1282"/>
      <path d="M1316,524 L1298,560 L1296,568 L1302,562 L1320,526 Z"/>
    </g>
  </g>

  <!-- note: language test -->
  <g class="note-box">
    <path class="note" d="M130,935 H682 V965 L697,982 L682,999 V1120 H130 Z"/>
    <text class="note-text">
      <tspan x="151" y="965">L’étudiant devra à cette date avoir déjà</tspan>
      <tspan x="151" y="993">passer le test KEL ou le MRT pour</tspan>
      <tspan x="151" y="1021">pouvoir être à temps pour les</tspan>
      <tspan x="151" y="1049">inscriptions universitaires. Il faut</tspan>
      <tspan x="151" y="1077">compter 6 semaines pour le test Kel et 2 à 3</tspan>
      <tspan x="151" y="1105">semaines pour obtenir les résultats des tests.</tspan>
    </text>
    <rect class="icon-tile" x="578" y="948" width="82" height="84" rx="5"/>
    <g class="icon-line">
      <rect x="596" y="960" width="46" height="60" rx="2"/>
      <circle cx="607" cy="972" r="4"/>
      <path d="M616,968 H634 M616,974 H634"/>
      <path d="M602,988 L605,991 L610,985 M616,988 H634"/>
      <path d="M602,1004 L605,1007 L610,1001 M616,1004 H634"/>
    </g>
  </g>

  <!-- note: start of term -->
  <g class="note-box">
    <path class="note" d="M1086,941 H1248 L1266,926 L1284,941 H1365 V1064 H1086 Z"/>
    <text class="note-text">
      <tspan x="1106" y="996">Rentrée</tspan>
      <tspan x="1106" y="1024">universitaire</tspan>
    </text>
    <rect class="icon-tile" x="1261" y="963" width="83" height="83" rx="5"/>
    <g class="icon-line">
      <path d="M1276,976 H1318 V1032 H1290 L1276,1010 Z"/>
      <circle cx="1311" cy="1008" r="8"/>
      <path d="M1306,1015 L1303,1028 L1311,1023 L1319,1028 L1316,1015"/>
    </g>
  </g>
</svg>
</body>
</html>
```